Advertisement Design Project: Print Ad

I need a print ad for a local boutique ski shop.
Size 5.43 inches wide by 5 inches high
full color
I am looking for a couple of options to market the following:
A: Kids Ski seasonal rental package
and/or
B:Early Season sales promotion
idea 1: "Be the first to check out this season's gear"
idea 2: "Looks you can take from the slopes to the streets"
idea 3: "The newer your gear, the better the performance"
idea 4: "Start off the new year with new gear"
OR YOUR COPY SUGGESTIONS
We would like a photo in the ad as well.
Need to include:
Our Name: Tarvell Ski Shop
Our address: 2847 N Marrow Lane, 3 blocks South of Cresthaven Commons in Quillstone Plaza
Target Market(s)
Families and Sports enthusiasts
Industry/Entity Type
Boutique
Look and feel

```html
<!DOCTYPE html>
<html lang="en">
<head>
<meta charset="utf-8">
<title>Tarvell Ski Shop – This Season's Gear</title>
<link rel="stylesheet" href="https://fonts.googleapis.com/css2?family=Bangers&family=Raleway:wght@300;500&display=swap">
<style>
  :root {
    --paper: #ffffff;
    --navy: #253a8a;
    --frame: #2c3a8f;
    --blue-deep: #22408f;
    --blue-light: #5fb2e4;
    --ink: #111111;
    --grey: #6b6b6d;
    --flame-hot: #f05a28;
    --flame-warm: #f7a43c;
    --suit-light: #f4f4f4;
    --suit-shade: #9a9a9a;
  }
  html, body {
    margin: 0;
    padding: 0;
    width: 901px;
    height: 1200px;
    overflow: hidden;
    background: var(--paper);
  }
  .ad {
    position: relative;
    width: 901px;
    height: 1200px;
    background: var(--paper);
  }
  .ad-frame {
    position: absolute;
    left: 38px;
    top: 38px;
    width: 822px;
    height: 1084px;
    border: 2px solid var(--frame);
    box-sizing: border-box;
  }
  .hero {
    position: absolute;
    left: 48px;
    top: 50px;
    width: 786px;
    height: 793px;
    overflow: hidden;
    background: radial-gradient(ellipse 420px 460px at 392px 545px, var(--blue-light) 0%, #3a78c4 40%, var(--blue-deep) 85%);
  }
  .hero-figure {
    position: absolute;
    left: 22px;
    top: 100px;
    width: 320px;
    height: 680px;
  }
  .hero-flames {
    position: absolute;
    left: 432px;
    top: 384px;
    width: 330px;
    height: 112px;
  }
  .headline {
    position: absolute;
    left: 357px;
    top: 82px;
    margin: 0;
    font-family: "Bangers", "Impact", sans-serif;
    font-weight: 400;
    color: var(--paper);
    font-size: 64px;
    line-height: 72px;
    letter-spacing: 5px;
    white-space: nowrap;
    transform: skewX(-4deg);
    text-shadow:
      3px 0 0 var(--ink), -3px 0 0 var(--ink), 0 3px 0 var(--ink), 0 -3px 0 var(--ink),
      2px 2px 0 var(--ink), -2px 2px 0 var(--ink), 2px -2px 0 var(--ink), -2px -2px 0 var(--ink),
      4px 4px 0 var(--ink);
  }
  .headline span { display: block; }
  .headline .headline-key {
    position: absolute;
    left: 120px;
    top: 310px;
    font-size: 96px;
    line-height: 90px;
    letter-spacing: 8px;
  }
  .brand {
    position: absolute;
    left: 48px;
    top: 843px;
    width: 786px;
    height: 144px;
    display: flex;
    align-items: center;
    justify-content: center;
  }
  .brand-name {
    font-family: "Raleway", "Helvetica", sans-serif;
    font-weight: 500;
    font-size: 84px;
    color: var(--grey);
    letter-spacing: -1px;
    margin-top: -10px;
  }
  .contact {
    position: absolute;
    left: 48px;
    top: 987px;
    width: 786px;
    height: 127px;
    background: var(--navy);
    color: var(--paper);
    font-family: "Raleway", "Helvetica", sans-serif;
    font-weight: 300;
    font-size: 23px;
    line-height: 29px;
    text-align: center;
    display: flex;
    flex-direction: column;
    justify-content: center;
    margin: 0;
    font-style: normal;
  }
</style>
</head>
<body>
  <main class="ad">
    <div class="ad-frame"></div>

    <section class="hero">
      <svg class="hero-figure" role="img" aria-label="Illustration of a snowboarder in a white winter suit and goggles riding down toward the viewer" viewBox="0 0 320 680">
        <defs>
          <linearGradient id="suit-tone" x1="0" y1="0" x2="1" y2="1">
            <stop offset="0" stop-color="var(--suit-light)" stop-opacity="0.55"/>
            <stop offset="1" stop-color="var(--suit-shade)" stop-opacity="0.35"/>
          </linearGradient>
        </defs>
        <rect x="0" y="0" width="320" height="680" rx="24" fill="url(#suit-tone)"/>
      </svg>

      <svg class="hero-flames" role="img" aria-label="Decorative orange flames behind the word Gear" viewBox="0 0 330 112">
        <defs>
          <linearGradient id="flame-tone" x1="0" y1="0" x2="0" y2="1">
            <stop offset="0" stop-color="var(--flame-hot)"/>
            <stop offset="1" stop-color="var(--flame-warm)"/>
          </linearGradient>
        </defs>
        <rect x="0" y="0" width="330" height="112" rx="40" fill="url(#flame-tone)" opacity="0.85"/>
      </svg>

      <h1 class="headline">
        <span>Be</span>
        <span>The first to</span>
        <span>check out</span>
        <span>this season's</span>
        <span class="headline-key">Gear</span>
      </h1>
    </section>

    <div class="brand">
      <span class="brand-name">Tarvell</span>
    </div>

    <address class="contact">
      <span>Tarvell Ski Shop</span>
      <span>Our address: 2847 N Marrow Lane,</span>
      <span>3 blocks South of Cresthaven Commons in Quillstone Plaza</span>
    </address>
  </main>
</body>
</html>
```